Chatterwall and Glimmerly advertising

We need Chatterwall and Glimmerly ads. Simple ad with Alaska themed background.
This ad is to introduce our new KESTREL Internet service.
--Speeds to 500 mpbs
-- Packages start at only $89.99 for speeds to 100mbps
-- Fiber Optic based connection, Not satellite
-- Extreme low latency, consistent speeds
--FREE equipment, FREE Installation, FREE wifi router, First month of service FREE

```html
<!DOCTYPE html>
<html lang="en">
<head>
<meta charset="utf-8">
<title>KESTREL Internet Service</title>
<link href="https://fonts.googleapis.com/css2?family=Arimo:ital,wght@0,400;0,700;1,400&display=swap" rel="stylesheet">
<style>
  :root {
    --night: #123e74;
    --deep: #24558f;
    --dusk: #5f6aa0;
    --warm: #e3a27a;
    --violet: #8a6aa8;
    --snow: #8fa9d2;
    --tile-top: #13294a;
    --tile-bottom: #1c3f6c;
    --ink: #ffffff;
    --badge-ink: #111111;
    --badge-bg: #ffffff;
  }
  * { margin: 0; padding: 0; box-sizing: border-box; }
  html, body { width: 1200px; height: 1200px; overflow: hidden; }
  body { font-family: "Arimo", Arial, sans-serif; color: var(--ink); }

  .ad {
    position: relative;
    width: 1200px;
    height: 1200px;
    overflow: hidden;
  }
  .ad__scene {
    position: absolute;
    inset: 0;
    background:
      linear-gradient(180deg, rgba(18,62,116,0) 55%, rgba(143,169,210,0.45) 78%, rgba(36,85,143,0.9) 100%),
      linear-gradient(110deg, var(--night) 0%, var(--deep) 40%, var(--dusk) 62%, var(--warm) 82%, var(--violet) 100%);
  }

  .brand-tile {
    position: absolute;
    left: 58px;
    top: 73px;
    width: 487px;
    height: 254px;
    background: linear-gradient(160deg, var(--tile-top) 0%, var(--tile-bottom) 100%);
  }
  .brand-tile__name {
    position: absolute;
    left: 44px;
    bottom: 44px;
    font-size: 66px;
    font-weight: 400;
    letter-spacing: 2px;
    line-height: 1;
  }

  .headline {
    position: absolute;
    left: 63px;
    top: 396px;
    font-size: 61px;
    font-weight: 700;
    line-height: 1;
    white-space: nowrap;
  }
  .speed-lead {
    position: absolute;
    left: 65px;
    top: 474px;
    font-size: 38px;
    font-weight: 700;
    line-height: 1;
  }
  .speed-value {
    position: absolute;
    left: 58px;
    top: 512px;
    font-size: 106px;
    font-weight: 700;
    line-height: 1;
    letter-spacing: -1px;
  }

  .features {
    position: absolute;
    left: 48px;
    top: 672px;
    width: 1110px;
    list-style: none;
    font-size: 39.5px;
    font-style: italic;
    line-height: 57px;
  }
  .features li {
    position: relative;
    padding-left: 41px;
  }
  .features li::before {
    content: "•";
    position: absolute;
    left: 0;
    font-style: normal;
    font-size: 30px;
  }

  .provider-badge {
    position: absolute;
    left: 681px;
    top: 1025px;
    width: 476px;
    height: 136px;
    background: var(--badge-bg);
  }
  .provider-badge__name {
    position: absolute;
    left: 6px;
    right: 6px;
    bottom: 14px;
    text-align: center;
    font-size: 58px;
    font-weight: 700;
    color: var(--badge-ink);
    line-height: 1;
    white-space: nowrap;
  }
</style>
</head>
<body>
  <main class="ad">
    <div class="ad__scene" role="img" aria-label="Snowy Alaskan landscape at sunrise with mountains, spruce trees and a snow-covered trail"></div>

    <div class="brand-tile" role="img" aria-label="Night sky image behind the KESTREL name">
      <span class="brand-tile__name">KESTREL</span>
    </div>

    <h1 class="headline">KESTREL Internet Service</h1>
    <p class="speed-lead">Speeds to</p>
    <p class="speed-value">500 mbps</p>

    <ul class="features">
      <li>Packages start at only $89.99 for speeds to 100mbps</li>
      <li>Fiber Optic based connection, Not satellite</li>
      <li>Extreme low latency, consistent speeds</li>
      <li>FREE equipment, FREE Installation, FREE wifi router, First month of service FREE</li>
    </ul>

    <div class="provider-badge">
      <span class="provider-badge__name">Northvale Link</span>
    </div>
  </main>
</body>
</html>
```